Project Manager Business Card for Top Architectural Firm

Update and design a stunning Senior Project Manager Business Card

MARCO T. DRUMMOND II
Senior Project Manager

H A L C Y O N
A R C H I T E C T U R E L L C.
www.HalcyonGrandEstates.example
4127 NW 52nd Ter. Suite 2308
Miami, FL 33148
C: (305) 555-0184
mdrummond.halcyongrandestates@mailbox.example

Looking to have the logo to be UV Spot ink printed and to be prominent.

Target Market(s)

High end real estate architecture construction

Industry/Entity Type

Architect

Contact Information for Business Card

MARCO T. DRUMMOND II
Senior Project Manager

H A L C Y O N
Miami, FL 33148
C: (305) 555-0184

Font styles to use
Sans Serif

Colors

Designer to choose colors to be used in the design.

Requirements
Must have
• Prominent Logo

```html
<!DOCTYPE html>
<html lang="en">
<head>
<meta charset="utf-8">
<title>Halcyon Architecture – Business Card</title>
<link rel="stylesheet" href="https://fonts.googleapis.com/css2?family=Saira:wght@400&display=swap">
<style>
  :root {
    --page-bg: #d9d6d1;
    --card-light: #eceef1;
    --card-mid: #dfe2e6;
    --strip: #3d4f67;
    --panel-dark: #182f50;
    --panel-mid: #123a6b;
    --panel-light: #2566a6;
    --panel-text: #cdd6e1;
    --brand-ink: #2c3038;
    --brand-dot: #2f6aa3;
  }
  * { margin: 0; padding: 0; box-sizing: border-box; }
  html, body {
    width: 1200px; height: 970px; overflow: hidden;
    background: var(--page-bg);
    font-family: "Saira", sans-serif;
  }
  .card {
    position: absolute; left: 50px; top: 180px;
    width: 1100px; height: 611px; border-radius: 30px;
    background: linear-gradient(180deg, var(--card-light), var(--card-mid));
    box-shadow: 0 10px 30px rgba(0,0,0,.18);
    overflow: hidden;
  }
  .side-strip {
    position: absolute; left: 2px; top: 69px; width: 61px; height: 480px;
    background: var(--strip); border-radius: 0 16px 16px 0;
  }
  .brand {
    position: absolute; left: 63px; top: 120px; width: 377px;
    text-align: center; color: var(--brand-ink); font-weight: 400;
  }
  .brand-dot {
    width: 130px; height: 130px; border-radius: 50%;
    background: var(--brand-dot); margin: 0 auto 40px;
  }
  .brand-name { font-size: 64px; line-height: 1; letter-spacing: 8px; }
  .brand-sub { font-size: 19px; letter-spacing: 5px; margin-top: 12px; }
  .info-panel {
    position: absolute; left: 440px; top: 69px; width: 660px; height: 480px;
    border-radius: 16px 0 0 16px;
    background: linear-gradient(100deg, var(--panel-dark) 0%, var(--panel-mid) 55%, var(--panel-light) 100%);
    color: var(--panel-text);
  }
  .person-name {
    position: absolute; left: 51px; top: 66px;
    font-size: 40px; line-height: 1; letter-spacing: 1px;
  }
  .person-title {
    position: absolute; left: 52px; top: 110px;
    font-size: 26px; line-height: 1; letter-spacing: .5px;
  }
  .contact-list { position: absolute; left: 58px; top: 236px; list-style: none; }
  .contact-item {
    display: flex; align-items: flex-start; gap: 13px;
    font-size: 25px; line-height: 30px; margin-bottom: 5px;
  }
  .contact-item.email { font-size: 21.5px; }
  .contact-icon { width: 20px; height: 20px; flex: none; margin-top: 5px; fill: var(--panel-text); }
</style>
</head>
<body>
  <div class="card">
    <div class="side-strip"></div>

    <div class="brand">
      <div class="brand-dot"></div>
      <div class="brand-name">HALCYON</div>
      <div class="brand-sub">ARCHITECTURE LLC.</div>
    </div>

    <div class="info-panel">
      <div class="person-name">MARCO T. DRUMMOND II</div>
      <div class="person-title">Senior Project Manager</div>

      <ul class="contact-list">
        <li class="contact-item">
          <svg class="contact-icon" viewBox="0 0 20 20"><path d="M5 1h10a1 1 0 0 1 1 1v16a1 1 0 0 1-1 1H5a1 1 0 0 1-1-1V2a1 1 0 0 1 1-1zm1 2v11h8V3zm4 12.5a1.2 1.2 0 1 0 0 2.4 1.2 1.2 0 0 0 0-2.4z"/></svg>
          <span>(305) 555-0184</span>
        </li>
        <li class="contact-item email">
          <svg class="contact-icon" viewBox="0 0 20 20"><path d="M1 4h18v12H1zm2 2v.3l7 5 7-5V6zm0 2.7V14h14V8.7l-7 5z"/></svg>
          <span>mdrummond.halcyongrandestates@mailbox.example</span>
        </li>
        <li class="contact-item">
          <svg class="contact-icon" viewBox="0 0 20 20"><path d="M10 1a9 9 0 1 0 0 18 9 9 0 0 0 0-18zm0 1.6c.9 0 2 1.7 2.5 4.4h-5C8 4.3 9.1 2.6 10 2.6zM7.3 8.5h5.4a17 17 0 0 1 0 3H7.3a17 17 0 0 1 0-3zm-1.5 0a19 19 0 0 0 0 3H2.8a7.4 7.4 0 0 1 0-3zm8.4 0h3a7.4 7.4 0 0 1 0 3h-3a19 19 0 0 0 0-3zM10 17.4c-.9 0-2-1.7-2.5-4.4h5c-.5 2.7-1.6 4.4-2.5 4.4z"/></svg>
          <span>www.HalcyonGrandEstates.example</span>
        </li>
        <li class="contact-item">
          <svg class="contact-icon" viewBox="0 0 20 20"><path d="M10 1a6 6 0 0 0-6 6c0 4.5 6 12 6 12s6-7.5 6-12a6 6 0 0 0-6-6zm0 8.3a2.3 2.3 0 1 1 0-4.6 2.3 2.3 0 0 1 0 4.6z"/></svg>
          <span>4127 NW 52nd Ter. Suite 2308<br>Miami, FL 33148</span>
        </li>
      </ul>
    </div>
  </div>
</body>
</html>
```